New Website Deisgn. Guaranteed Project.

I would like a site similar to this: http://givewheelsheal.org.

old site: http://autosforrelief.org

Create a professional website; a car donation site seeking leads to return calls.

Please see http://givewheelsheal.org for the concept I am after.

The webpage should have a professional feel. The pages to include are 'Home', 'About us' and 'Get Started'

Industry/Entity Type

It Professional

Coding

Coded - Design and coding required

Number of Pages Required

1 page

```html
<!DOCTYPE html>
<html lang="en">
<head>
<meta charset="utf-8">
<title>Wheels for Hope – Donate Your Car</title>
<link href="https://fonts.googleapis.com/css2?family=Signika:wght@400;600&family=Open+Sans:wght@400;600;700&display=swap" rel="stylesheet">
<style>
:root{
  --blue:#4f7db0;
  --blue-dark:#3f6a98;
  --orange:#cf8d1b;
  --orange-dark:#b97a12;
  --ink:#1e1e1e;
  --muted:#555;
  --frame:#e4e4e6;
  --lavender:#d9d3e0;
  --line:#cfcfcf;
  --white:#fff;
}
*{margin:0;padding:0;box-sizing:border-box}
html,body{width:1200px;height:2659px;overflow:hidden;background:var(--frame)}
body{font-family:"Open Sans",Arial,sans-serif;color:var(--ink);position:relative}
.page{position:absolute;left:14px;top:14px;width:1172px;height:2631px;background:var(--white);overflow:hidden}
.abs{position:absolute}
.heading{font-family:"Signika",Arial,sans-serif}

/* header */
.brand{left:30px;top:62px;font-family:"Signika",sans-serif;font-weight:600;font-size:32px;color:var(--blue)}
.call{right:30px;top:26px;display:flex;align-items:center;gap:12px}
.call-label{font-weight:700;font-size:16px;color:#444;line-height:1}
.call-num{font-weight:700;font-size:25px;color:var(--blue);line-height:1.1}
.nav{left:340px;top:96px;width:832px;height:37px;background:var(--blue);display:flex;padding-left:100px}
.nav a{display:block;color:var(--white);font-size:14px;font-weight:700;text-decoration:none;padding:0 24px;line-height:37px;text-transform:uppercase}
.nav a.active{background:var(--orange)}
.nav-cut{left:320px;top:96px;width:40px;height:37px;background:var(--blue);transform:skewX(-30deg)}

/* hero */
.hero-art{left:0;top:133px;width:1172px;height:518px;background:linear-gradient(180deg,#cfe2ee 0%,#eef3f5 55%,#e9ecef 100%)}
.hero-people{left:30px;top:175px;width:434px;height:476px;background:linear-gradient(160deg,#d8c27a,#6fae4c 75%);border-radius:4px}
.hero-cars{left:430px;top:380px;width:330px;height:270px;background:linear-gradient(180deg,#dadada,#9a2b2b 85%);border-radius:30px 30px 4px 4px;opacity:.85}
.hero-title{left:408px;top:232px;color:var(--blue);font-size:30px;line-height:1.1}
.hero-title b{display:block;color:var(--orange);font-size:44px;font-weight:600}

.form{left:780px;top:210px;width:360px;height:406px;background:rgba(226,218,232,.9);padding:28px 18px 0}
.form-arc{left:780px;top:185px}
.form h2{font-size:16px;font-weight:700;text-align:center;line-height:1.3;color:#333;margin-bottom:18px}
.row{display:flex;gap:18px;margin-bottom:11px}
.field{flex:1;height:30px;background:#eceaf0;border:1px solid #d4d0da;border-radius:2px;font-size:12px;color:#666;line-height:28px;padding-left:10px;position:relative}
.field.select::after{content:"";position:absolute;right:10px;top:11px;border:5px solid transparent;border-top-color:#555}
.btn{margin-top:14px;height:46px;background:var(--orange);color:var(--white);font-weight:700;font-size:17px;text-align:center;line-height:46px;border-radius:2px}

.band{left:0;top:651px;width:1172px;height:80px;background:var(--blue);color:var(--white);font-weight:700;font-size:21px;text-align:center;line-height:80px}
.divider{height:6px;width:414px;left:379px}

/* how it works */
.section-title{width:100%;text-align:center;font-family:"Signika",sans-serif;font-weight:600;font-size:30px}
.step-title{font-size:16px;font-weight:700}
.step-text{font-size:12px;font-weight:600;color:var(--blue);line-height:1.35;width:270px}
.step-list{font-size:12px;font-weight:600;color:#444;line-height:1.4;margin-top:12px}

/* charities */
.charity-bg{left:0;top:1085px;width:1172px;height:369px;background:linear-gradient(90deg,#fff 0%,#f4f3f2 70%,#ece9e7 100%)}
.partner{left:44px;top:1262px;display:flex;align-items:center;gap:12px;font-family:"Signika",sans-serif;font-size:23px;color:var(--ink)}
.partner i{width:60px;height:60px;background:var(--orange);display:block}
.charity-text{left:417px;top:1200px;width:352px;font-size:13.5px;line-height:21px;color:#444}
.child-photo{left:796px;top:1085px;width:360px;height:369px;background:radial-gradient(ellipse at 45% 40%,#f3dccc 0%,#e7cfc0 40%,#6b4b3f 80%,#e9e6e4 100%)}

/* tax */
.tax{left:0;top:1454px;width:1172px;height:393px;background:linear-gradient(120deg,#5a88b8,#4a79aa 50%,#5f8dba)}
.tax-title{top:1525px;color:var(--white);font-size:31px;font-weight:400;text-align:center;width:100%}
.tax-sub{top:1565px;width:100%;text-align:center;color:var(--white);font-size:13px;font-weight:700}
.tab{left:59px;width:333px;height:40px;background:#eef2f7;color:var(--blue);font-size:14px;font-weight:600;line-height:40px;padding-left:20px;border:1px solid #9db4cc}
.tab.active{background:#dfe7f1}
.tax-rule{left:392px;top:1615px;width:2px;height:185px;background:#e8eef5}
.tax-copy{left:440px;top:1630px;width:520px;color:var(--white);font-size:13.5px;line-height:1.5}
.tax-copy p{margin-bottom:20px}
.badge{left:979px;top:1635px}

/* faq */
.faq-title{top:1907px;color:#9a9aa2;font-weight:400}
.faq-col{top:1988px;width:412px}
.faq-col li{list-style:none;font-size:13.5px;font-weight:600;padding:6px 0 7px;border-bottom:1px solid var(--line);line-height:1.35}

/* footer */
.footer-bg{left:0;top:2392px;width:1172px;height:209px;background:var(--lavender)}
.footer-blue{left:0;top:2392px}
.ft-h{font-size:13px;font-weight:700;color:var(--white);margin-bottom:12px}
.ft-p{font-size:11.5px;line-height:1.45;color:var(--white);font-weight:600}
.ft-links a{display:block;color:var(--white);text-decoration:none;font-size:11.5px;font-weight:600;line-height:1.6}
.ft-brand{left:830px;top:2482px;font-family:"Signika",sans-serif;font-weight:600;font-size:32px;color:var(--blue)}
.copy{left:0;top:2601px;width:1172px;height:30px;text-align:center;font-size:11px;font-weight:700;line-height:30px;color:#333}
</style>
</head>
<body>
<div class="page">

  <!-- header -->
  <div class="abs brand">Wheels for Hope</div>
  <div class="abs call">
    <svg width="40" height="40" viewBox="0 0 40 40"><circle cx="20" cy="20" r="18" fill="none" stroke="#4f7db0" stroke-width="2.5"/><path d="M14 11c2 0 3 4 3 5s-2 2-2 3c1 2 3 5 6 6 1 0 2-2 3-2s5 1 5 3-2 4-4 4c-7 0-15-8-15-15 0-2 2-4 4-4z" fill="#4f7db0"/></svg>
    <div><div class="call-label">CALL TODAY TO DONATE</div><div class="call-num">1-800-555-0147</div></div>
  </div>
  <div class="abs nav-cut"></div>
  <nav class="abs nav">
    <a class="active" href="#">Home</a><a href="#">How It Works</a><a href="#">About Us</a><a href="#">FAQ</a><a href="#">Get Started</a>
  </nav>

  <!-- hero -->
  <div class="abs hero-art" role="img" aria-label="Light city skyline sketch behind the hero area"></div>
  <div class="abs hero-people" role="img" aria-label="Photo of a smiling mother holding her young daughter"></div>
  <div class="abs hero-cars" role="img" aria-label="Photo of a white pickup truck and a red classic sports car"></div>
  <h1 class="abs hero-title heading" style="font-weight:400">Donate Your Car to Fight<b>Children's Cancer</b></h1>

  <svg class="abs form-arc" width="360" height="40" viewBox="0 0 360 40"><path d="M0 38 Q180 -10 360 38 L360 40 L0 40Z" fill="rgba(226,218,232,.9)"/><path d="M0 38 Q180 -10 360 38" fill="none" stroke="#cf8d1b" stroke-width="5"/></svg>
  <form class="abs form">
    <h2>Donating is Easy &amp; Makes a Real<br>Difference. Fill out the form below<br>to instantly donate online.</h2>
    <div class="row"><div class="field">First Name</div><div class="field">Last Name</div></div>
    <div class="row"><div class="field">Phone Number</div></div>
    <div class="row"><div class="field">Email Address</div></div>
    <div class="row"><div class="field select">Choose Year</div><div class="field select">Choose Make</div></div>
    <div class="row"><div class="field">Vehicle Model</div><div class="field">Zip Code</div></div>
    <div class="btn">Click to Donate your Car</div>
  </form>

  <div class="abs band">Donate Your Car, Truck, RV. Boat, Motorcycle, or ATV in all 50 states and make a difference.</div>
  <div class="abs divider" style="top:731px;background:var(--orange)"></div>

  <!-- how it works -->
  <h2 class="abs section-title" style="top:795px;color:var(--orange)">How It Works</h2>

  <svg class="abs" style="left:55px;top:867px" width="72" height="94" viewBox="0 0 72 94"><rect x="10" y="6" width="56" height="12" fill="#cf8d1b"/><rect x="26" y="26" width="40" height="12" fill="#cf8d1b"/><rect x="26" y="46" width="40" height="12" fill="#cf8d1b"/><rect x="10" y="26" width="10" height="50" fill="#cf8d1b"/><path d="M6 88 L22 62 L30 70 Z" fill="#cf8d1b"/></svg>
  <div class="abs" style="left:137px;top:912px">
    <div class="step-title">1. Fill out the simple form</div>
    <div class="step-text">Use our online vehicle donation form to submit your information.</div>
    <div class="step-list">- Donating your vehicle is easy<br>- Vehicle donations accepted nationwide</div>
  </div>

  <svg class="abs" style="left:420px;top:875px" width="96" height="70" viewBox="0 0 96 70"><rect x="4" y="24" width="50" height="28" rx="3" fill="#cf8d1b"/><path d="M54 30 H76 L90 44 V52 H54Z" fill="#cf8d1b"/><circle cx="20" cy="56" r="9" fill="#fff" stroke="#cf8d1b" stroke-width="4"/><circle cx="74" cy="56" r="9" fill="#fff" stroke="#cf8d1b" stroke-width="4"/><path d="M10 24 L30 6" stroke="#cf8d1b" stroke-width="4"/></svg>
  <div class="abs" style="left:530px;top:912px">
    <div class="step-title">2. Schedule your free pick-up</div>
    <div class="step-text">We will arrange to pick up your vehicle when it is most convenient for you.</div>
    <div class="step-list">- Any vehicle is accepted<br>- Free towing for your charity vehicle<br>&nbsp;&nbsp;donation with 24 hours</div>
  </div>

  <svg class="abs" style="left:823px;top:868px" width="66" height="94" viewBox="0 0 66 94"><rect x="12" y="4" width="48" height="66" fill="#fff" stroke="#cf8d1b" stroke-width="2.5"/><rect x="4" y="12" width="48" height="66" fill="#fff" stroke="#cf8d1b" stroke-width="2.5"/><text x="28" y="44" text-anchor="middle" font-size="22" font-weight="700" fill="#cf8d1b" font-family="Open Sans,sans-serif">$</text><path d="M12 56 H44 M12 64 H44" stroke="#cf8d1b" stroke-width="2.5"/></svg>
  <div class="abs" style="left:907px;top:912px">
    <div class="step-title">3. Receive tax deduction</div>
    <div class="step-text" style="color:#333">Once the vehicle donation is complete, you will receive your tax deductable vehicle donation receipt.</div>
  </div>

  <!-- charities -->
  <div class="abs charity-bg"></div>
  <div class="abs divider" style="top:1085px;background:#a08a7e"></div>
  <h2 class="abs section-title" style="top:1136px;color:#a08a7e;left:0;width:1172px">Charities We Work With</h2>
  <div class="abs partner"><i></i>Bright Futures Kids Fund</div>
  <p class="abs charity-text">Bright Futures Kids Fund's mission is to make a positive difference in the lives of children and their families affected by cancer, by helping people with limited finances and special needs receive funds to assist in meeting their financial needs and to reduce the stress and strain that managing cancer can cause. The fund also provides funding toward research for children's cancers as well as fosters health wellness and a whole-body approach to cancer treatment and recovery.</p>
  <div class="abs child-photo" role="img" aria-label="Photo of a young child undergoing cancer treatment"></div>

  <!-- tax -->
  <div class="abs tax" role="img" aria-label="Blue-tinted photo of tax paperwork, a pen and a calculator"></div>
  <h2 class="abs tax-title heading">Tax Deduction Information For Your Car Donation</h2>
  <div class="abs tax-sub">The IRS has set the rules for the tax deduction of your vehicle donation</div>
  <div class="abs tab" style="top:1640px">If Your Car Donation Sells for $500 Or Less</div>
  <div class="abs tab active" style="top:1690px">If Your Car Donation Sells for $501 Or More</div>
  <div class="abs tab" style="top:1740px">How to file your taxes</div>
  <div class="abs tax-rule"></div>
  <div class="abs tax-copy">
    <p>You can claim the exact amount for which the vehicle is sold.</p>
    <p>When you donate your car, we will provide you with a tax deductible receipt.</p>
    <p>Within 30 days from the sale of your vehicle we will provide you with<br>a 1098-C form to submit with your taxes.</p>
  </div>
  <svg class="abs badge" width="136" height="136" viewBox="0 0 136 136"><circle cx="68" cy="68" r="64" fill="#fff" stroke="#5a88b8" stroke-width="4"/><circle cx="68" cy="68" r="56" fill="none" stroke="#5a88b8" stroke-width="1.5"/><text x="68" y="62" text-anchor="middle" font-family="Open Sans,sans-serif" font-weight="700" font-size="16" fill="#4f7db0">$501 or More</text><path d="M38 84 H98" stroke="#4f7db0" stroke-width="1.5"/><path d="M48 90 L54 80 H80 L88 88 H94 V94 H44 V90Z" fill="#4f7db0"/><circle cx="56" cy="95" r="4" fill="#fff" stroke="#4f7db0" stroke-width="2"/><circle cx="84" cy="95" r="4" fill="#fff" stroke="#4f7db0" stroke-width="2"/></svg>
  <div class="abs divider" style="top:1847px;background:#cfd3dc"></div>

  <!-- faq -->
  <h2 class="abs section-title faq-title">Frequently Asked Questions</h2>
  <ul class="abs faq-col" style="left:83px">
    <li>+ What types of vehicles can be donated?</li>
    <li>+ If my vehicle is not running, can I still donate?</li>
    <li>+ What paperwork do I need to donate my vehicle?</li>
    <li>+ Is my donated vehicle tax -deductible?</li>
    <li>+ What areas do you service?</li>
    <li>+ What documents do I need to donate a car to charity?</li>
    <li>+ What if the vehicle is not registered in my name?</li>
    <li>+ There are two people listed on the title, what should I do?</li>
    <li>+ The Title Is In A Deceased Person's Name. How do I complete<br>&nbsp;&nbsp;&nbsp;The Transfer Of Title?</li>
  </ul>
  <ul class="abs faq-col" style="left:677px">
    <li>+ How much will I receive as a tax deduction for my vehicle?</li>
    <li>+ How do you determine the value of my vehicle?</li>
    <li>+ When will I receive my tax receipt?</li>
    <li>+ How do I schedule a pick up?</li>
    <li>+ Who will pick up my vehicle?</li>
    <li>+ Do I have to be home when my vehicle is picked up?</li>
    <li>+ How quickly can my vehicle be picked up?</li>
    <li>+ Can you pick up my vehicle if it's not at my home?</li>
    <li>+ What will I receive at time of pick-up?</li>
  </ul>

  <!-- footer -->
  <div class="abs footer-bg"></div>
  <svg class="abs footer-blue" width="870" height="209" viewBox="0 0 870 209"><polygon points="0,0 855,0 730,209 0,209" fill="#4f7db0"/></svg>
  <div class="abs" style="left:75px;top:2425px;width:280px">
    <div class="ft-h">About Wheels For Hope</div>
    <p class="ft-p">We turn donated cars, trucks and boats into support for children fighting cancer and their families. Every vehicle helps fund care, comfort and research, and our team handles the towing and paperwork so giving stays simple for you, in every state and every season of the year.</p>
  </div>
  <div class="abs ft-links" style="left:385px;top:2425px">
    <div class="ft-h">Navigation</div>
    <a href="#">Home</a><a href="#">How It works</a><a href="#">About Us</a><a href="#">Faq</a><a href="#">Get Started</a>
  </div>
  <div class="abs" style="left:530px;top:2425px">
    <div class="ft-h">Contact Info</div>
    <div style="display:flex;gap:10px">
      <svg width="18" height="14" viewBox="0 0 18 14"><path d="M1 5 Q9 -2 17 5 L15 7 L12 5 V3 H6 V5 L3 7Z" fill="#fff"/><rect x="4" y="7" width="10" height="6" rx="1" fill="#fff"/></svg>
      <p class="ft-p" style="font-size:12.5px">CALL 1-800-555-0147<br>Live Operators Available<br>7 Days A Week</p>
    </div>
  </div>
  <div class="abs ft-brand">Wheels for Hope</div>
  <div class="abs copy">COPYRIGHT © 2017 WHEELS FOR HOPE. ALL RIGHTS RESERVED.</div>
</div>
</body>
</html>
```